Brevinor
Brevinor - Consulting
Use same font as used in my logo
It is up to you.
Simple
Lionel Brasquet
President
82 Thornwell Avenue Toronto, Ontario M4R 2J8
l.brasquet@brevinorhub.com
www.brevinorhub.com
Will be the same however in French

```html
<!DOCTYPE html>
<html lang="en">
<head>
<meta charset="utf-8">
<title>Brevinor Stationery</title>
<link href="https://fonts.googleapis.com/css2?family=Michroma&family=Open+Sans:wght@400;600&display=swap" rel="stylesheet">
<style>
  :root {
    --navy: #1f4e7a;
    --navy-dark: #163a5c;
    --steel: #6e7175;
    --paper: #ffffff;
    --flap-light: #f3f3f3;
    --edge: #d6d6d6;
    --ground: #e7e3dc;
    --ink: #55585c;
    --label: #4a4640;
  }
  * { margin: 0; padding: 0; box-sizing: border-box; }
  html, body { width: 1200px; height: 446px; overflow: hidden; }
  body { background: var(--ground); position: relative; font-family: "Open Sans", sans-serif; color: var(--ink); }
  .sheet { position: absolute; background: var(--paper); box-shadow: 0 1px 3px rgba(0,0,0,.25); overflow: hidden; }
  .brand { font-family: "Michroma", sans-serif; color: var(--navy); letter-spacing: .06em; white-space: nowrap; display: flex; align-items: center; gap: 4px; }
  .brand .dot { width: 6px; height: 6px; border-radius: 50%; background: var(--navy); }
  .band { position: absolute; left: 0; right: 0; bottom: 0; background: linear-gradient(180deg, #3a6f9f, var(--navy-dark)); }
  .fine { font-size: 4px; line-height: 1.5; color: var(--ink); white-space: nowrap; }
  .label { position: absolute; font-family: "Michroma", sans-serif; font-size: 5px; letter-spacing: .12em; color: var(--label); text-transform: uppercase; white-space: nowrap; }
  .set-title { left: 12px; top: 184px; }

  .card-front { left: 19px; top: 223px; width: 89px; height: 67px; }
  .card-front .brand { position: absolute; left: 7px; top: 10px; font-size: 7px; }
  .card-front .brand .dot { width: 4px; height: 4px; }
  .card-front .who { position: absolute; left: 36px; top: 30px; font-size: 3.4px; }
  .card-front .band { height: 3px; }
  .card-back { left: 19px; top: 326px; width: 89px; height: 65px; }
  .card-back .brand { position: absolute; left: 0; right: 0; top: 24px; justify-content: center; font-size: 8px; }
  .card-back .brand .dot { width: 4px; height: 4px; }
  .card-back .band { height: 8px; }

  .letter { top: 24px; height: 396px; }
  .letter-one { left: 252px; width: 199px; }
  .letter-one .brand { position: absolute; left: 18px; top: 20px; font-size: 10px; }
  .letter-one .contact { position: absolute; right: 18px; top: 20px; }
  .letter-two { left: 475px; width: 202px; }
  .letter-two .brand { position: absolute; left: 0; right: 0; top: 22px; justify-content: center; font-size: 10px; }
  .letter-two .contact { position: absolute; left: 0; right: 0; bottom: 14px; text-align: center; font-size: 3.6px; }
  .letter .band { height: 7px; }

  .envelope-backs { position: absolute; left: 840px; top: 10px; }
  .envelope-front { left: 799px; top: 257px; width: 329px; height: 151px; }
  .envelope-front .brand { position: absolute; left: 16px; top: 14px; font-size: 10px; }
  .envelope-front .return { position: absolute; left: 16px; top: 34px; }
  .envelope-front .band { height: 6px; }
</style>
</head>
<body>
  <div class="label set-title">Stationery Concepts</div>

  <section class="sheet card-front" aria-label="Business card front">
    <div class="brand"><span class="dot"></span>BREVINOR</div>
    <div class="who fine">
      <strong>Lionel Brasquet</strong><br>President<br>Tel 416 555 0142<br>l.brasquet@brevinorhub.com<br>www.brevinorhub.com
    </div>
    <div class="band"></div>
  </section>
  <div class="label" style="left:22px;top:298px;">Business Card Front</div>

  <section class="sheet card-back" aria-label="Business card back">
    <div class="brand"><span class="dot"></span>BREVINOR</div>
    <div class="band"></div>
  </section>
  <div class="label" style="left:24px;top:398px;">Business Card Back</div>

  <section class="sheet letter letter-one" aria-label="Letterhead option 1">
    <div class="brand"><span class="dot"></span>BREVINOR</div>
    <div class="contact fine">
      82 Thornwell Avenue<br>Toronto, Ontario M4R 2J8<br>Tel 416 555 0142<br>www.brevinorhub.com
    </div>
    <div class="band"></div>
  </section>
  <div class="label" style="left:314px;top:432px;">Letterhead Option 1</div>

  <section class="sheet letter letter-two" aria-label="Letterhead option 2">
    <div class="brand"><span class="dot"></span>BREVINOR</div>
    <div class="contact fine">
      82 Thornwell Avenue, Toronto, Ontario M4R 2J8 &nbsp;·&nbsp; Tel 416 555 0142 &nbsp;·&nbsp; Fax 416 555 0143<br>l.brasquet@brevinorhub.com &nbsp;·&nbsp; www.brevinorhub.com
    </div>
    <div class="band"></div>
  </section>
  <div class="label" style="left:538px;top:432px;">Letterhead Option 2</div>

  <svg class="envelope-backs" width="292" height="280" viewBox="0 0 292 280" aria-label="Envelope backs">
    <rect x="2" y="2" width="288" height="100" fill="var(--paper)" stroke="var(--edge)"/>
    <path d="M2 2 H290 V34 Q146 90 2 34 Z" fill="var(--navy)"/>
    <rect x="2" y="88" width="288" height="100" fill="var(--paper)" stroke="var(--edge)"/>
    <path d="M2 88 H290 V120 Q146 176 2 120 Z" fill="var(--steel)"/>
    <rect x="2" y="174" width="288" height="100" fill="var(--paper)" stroke="var(--edge)"/>
    <path d="M2 174 H290 V206 Q146 262 2 206 Z" fill="var(--flap-light)" stroke="#cfcfcf"/>
  </svg>

  <section class="sheet envelope-front" aria-label="Envelope front">
    <div class="brand"><span class="dot"></span>BREVINOR</div>
    <div class="return fine">82 Thornwell Avenue<br>Toronto, Ontario M4R 2J8</div>
    <div class="band"></div>
  </section>
  <div class="label" style="left:1020px;top:432px;">Envelope Design</div>
</body>
</html>
```